The Marrow Lanterns Podcast

A logo that defines defiance. The "Marrow Lanterns" Podcast with Brent & Quill will revolve around people who have accomplished remarkable things in spite of odds being stacked against them. I want the logo to be simple, marketable, strong and bold, attractive to the eye on a mobile device. The hosts name will be part of the logo. I will give you full creative freedom to the artists to try to create something that is truly legendary and amazing. Please feel free to reach out if you have any questions.Podcast name: The Defying OnesHosts: Brent & Quill
Target Market(s)
Listeners interested in self growth, excitement, inspiration, fun.
Colors
Designer to choose colors to be used in the design.
Look and feel

```html
<!DOCTYPE html>
<html lang="en">
<head>
<meta charset="UTF-8">
<title>The Marrow Lanterns Podcast – Cover</title>
<link rel="stylesheet" href="https://fonts.googleapis.com/css2?family=Montserrat:wght@600;700;800&display=swap">
<style>
  :root {
    --page-bg: #ffffff;
    --space-deep: #0d1a22;
    --space-mid: #1c2f2c;
    --forest: #2f3f2a;
    --earth: #4a4a3a;
    --cloud: #8d979a;
    --title-light: #ffffff;
    --title-shade: #b9bcc0;
    --ring: #ffffff;
    --glow-core: #fff3d6;
    --glow-warm: #ffa640;
    --glow-deep: #e0620f;
  }
  * { margin: 0; padding: 0; box-sizing: border-box; }
  html, body {
    width: 1200px;
    height: 870px;
    overflow: hidden;
    background: var(--page-bg);
  }
  .canvas {
    position: relative;
    width: 1200px;
    height: 870px;
    display: flex;
    align-items: center;
    justify-content: center;
  }
  .cover {
    position: relative;
    width: 780px;
    height: 780px;
    overflow: hidden;
    font-family: "Montserrat", sans-serif;
  }
  .cover-scene {
    position: absolute;
    inset: 0;
    background:
      radial-gradient(ellipse at 85% 25%, rgba(141,151,154,0.35), transparent 40%),
      radial-gradient(ellipse at 80% 70%, rgba(74,74,58,0.55), transparent 50%),
      radial-gradient(ellipse at 25% 35%, rgba(47,63,42,0.7), transparent 55%),
      linear-gradient(160deg, var(--space-mid) 0%, var(--forest) 45%, var(--space-deep) 100%);
  }
  .cover-ring {
    position: absolute;
    inset: 0;
    width: 780px;
    height: 780px;
  }
  .cover-title {
    position: absolute;
    left: 0;
    right: 0;
    top: 218px;
    text-align: center;
    font-weight: 700;
    font-size: 96px;
    line-height: 100px;
    letter-spacing: 2px;
    text-transform: uppercase;
    background: linear-gradient(180deg, var(--title-light) 30%, var(--title-shade) 100%);
    -webkit-background-clip: text;
    background-clip: text;
    color: transparent;
    filter: drop-shadow(0 3px 6px rgba(0,0,0,0.45));
  }
  .cover-title span { display: block; }
  .cover-hosts {
    position: absolute;
    left: 0;
    right: 0;
    top: 668px;
    text-align: center;
    font-weight: 700;
    font-size: 31px;
    color: var(--title-light);
    text-shadow: 0 2px 6px rgba(0,0,0,0.6);
  }
</style>
</head>
<body>
<main class="canvas">
  <section class="cover">
    <div class="cover-scene" role="img" aria-label="Photo of an astronaut floating above a forested valley with clouds, seen from high above"></div>
    <svg class="cover-ring" viewBox="0 0 780 780" aria-hidden="true">
      <defs>
        <radialGradient id="glow" cx="0.5" cy="0.5" r="0.5">
          <stop offset="0" stop-color="var(--glow-core)" stop-opacity="1"/>
          <stop offset="0.25" stop-color="var(--glow-warm)" stop-opacity="0.75"/>
          <stop offset="0.6" stop-color="var(--glow-deep)" stop-opacity="0.25"/>
          <stop offset="1" stop-color="var(--glow-deep)" stop-opacity="0"/>
        </radialGradient>
        <filter id="soft" x="-20%" y="-20%" width="140%" height="140%">
          <feGaussianBlur stdDeviation="3"/>
        </filter>
      </defs>
      <ellipse cx="390" cy="150" rx="190" ry="60" fill="url(#glow)"/>
      <ellipse cx="390" cy="628" rx="170" ry="45" fill="url(#glow)" opacity="0.8"/>
      <circle cx="390" cy="390" r="238" fill="none" stroke="var(--glow-warm)" stroke-width="8" opacity="0.45" filter="url(#soft)"/>
      <circle cx="390" cy="390" r="238" fill="none" stroke="var(--ring)" stroke-width="4"/>
    </svg>
    <h1 class="cover-title">
      <span>The</span>
      <span>Marrow</span>
      <span>Lanterns</span>
    </h1>
    <p class="cover-hosts">Hosts: Brent &amp; Quill</p>
  </section>
</main>
</body>
</html>
```